Fixing all glass products,fitting security doors,flyscreens,splashbacks,glazing

Looking for perhaps a liitle happy chap carrying a glass panel with crach throught it and maybe the pane of glass 'hurting' so it had 'pain'???
Open to suggestions

Industry/Entity Type

Security

Contact Information for Business Card

Brisk Corner Fitters
Darren Holloway
Specialising in security doors,flyscreens,splashbacks
0417362048
darrenholloway518@mailbrook.net

```html
<!DOCTYPE html>
<html lang="en">
<head>
<meta charset="utf-8">
<title>Brisk Corner Fitters – Business Card</title>
<link href="https://fonts.googleapis.com/css2?family=PT+Sans&family=Source+Sans+3:wght@400;600&display=swap" rel="stylesheet">
<style>
  :root {
    --backdrop-inner: #5a5a5a;
    --backdrop-outer: #2e2e2e;
    --card-white: #ffffff;
    --card-haze: #e6e7e9;
    --title-blue: #1a70b8;
    --band-dark: #3a3b3e;
    --band-deep: #1f4fa3;
    --band-light: #22b0e6;
    --text-white: #ffffff;
    --art-pale: #dbeef6;
    --art-mid: #b9d3e6;
  }
  html, body {
    margin: 0;
    padding: 0;
    width: 1200px;
    height: 999px;
    overflow: hidden;
  }
  body {
    background: radial-gradient(ellipse at center, var(--backdrop-inner) 0%, var(--backdrop-outer) 100%);
    position: relative;
  }
  .card {
    position: absolute;
    left: 68px;
    top: 192px;
    width: 1064px;
    height: 614px;
    background: linear-gradient(to bottom, var(--card-haze) 0%, var(--card-white) 90px);
    overflow: hidden;
  }
  .card__title {
    position: absolute;
    left: 62px;
    top: 88px;
    margin: 0;
    font-family: "PT Sans", sans-serif;
    font-weight: 400;
    font-size: 70px;
    line-height: 90px;
    color: var(--title-blue);
  }
  .card__artwork {
    position: absolute;
    left: 659px;
    top: 53px;
    width: 361px;
    height: 295px;
    background: linear-gradient(160deg, var(--art-pale) 0%, var(--art-mid) 100%);
    border-radius: 4px;
  }
  .card__band {
    position: absolute;
    left: 0;
    top: 380px;
    width: 1064px;
    height: 234px;
  }
  .services {
    position: absolute;
    left: 42px;
    top: 464px;
    font-family: "Source Sans 3", sans-serif;
    color: var(--text-white);
    font-size: 26px;
    line-height: 37px;
  }
  .services__lead {
    font-weight: 600;
    display: block;
  }
  .contact {
    position: absolute;
    left: 582px;
    top: 478px;
    font-family: "Source Sans 3", sans-serif;
    color: var(--text-white);
    font-size: 29px;
    line-height: 47px;
  }
  .contact__row {
    display: flex;
    align-items: center;
    gap: 16px;
  }
  .contact__icon {
    width: 26px;
    height: 26px;
    flex: none;
  }
</style>
</head>
<body>
  <section class="card">
    <h1 class="card__title">Brisk Corner Fitters<br>Darren Holloway</h1>

    <div class="card__artwork" role="img" aria-label="Cartoon of two cheerful glaziers carrying a cracked pane of glass"></div>

    <svg class="card__band" viewBox="0 0 1064 234" aria-hidden="true">
      <defs>
        <radialGradient id="bandGlow" cx="0.5" cy="0.62" r="0.6" gradientTransform="scale(1,0.9)">
          <stop offset="0" stop-color="var(--band-light)"/>
          <stop offset="0.55" stop-color="#1a8fd3"/>
          <stop offset="1" stop-color="var(--band-deep)"/>
        </radialGradient>
      </defs>
      <path d="M0 50 Q532 -46 1064 50 L1064 234 L0 234 Z" fill="var(--band-dark)"/>
      <path d="M0 58 Q532 -30 1064 60 L1064 234 L0 234 Z" fill="url(#bandGlow)"/>
    </svg>

    <p class="services">
      <span class="services__lead">Specialising in</span>
      security doors, flyscreens<br>
      splashbacks
    </p>

    <div class="contact">
      <div class="contact__row">
        <svg class="contact__icon" viewBox="0 0 24 24" aria-hidden="true">
          <path fill="#fff" d="M6.6 2.5c.5-.2 1 0 1.3.4l2 3.2c.3.5.2 1.1-.2 1.4L8.2 8.8c.9 2.4 2.6 4.3 4.9 5.4l1.3-1.5c.4-.4 1-.5 1.4-.2l3.2 2c.5.3.6.9.4 1.4l-1 2.3c-.3.6-.9 1-1.6.9C9.9 18.3 4.8 13.1 4 6.2c-.1-.7.3-1.3.9-1.6z"/>
          <path fill="none" stroke="#fff" stroke-width="1.6" stroke-linecap="round" d="M14 3.5a6.5 6.5 0 0 1 6.5 6.5M14 7a3 3 0 0 1 3 3"/>
        </svg>
        <span>0417362048</span>
      </div>
      <div class="contact__row">
        <svg class="contact__icon" viewBox="0 0 24 24" aria-hidden="true">
          <path fill="#fff" d="M3 9l9-6 9 6v11H3z"/>
          <path fill="none" stroke="var(--band-light)" stroke-width="1.6" d="M4 10l8 5 8-5"/>
        </svg>
        <span>darrenholloway518@mailbrook.net</span>
      </div>
    </div>
  </section>
</body>
</html>
```